Awsome new website

We are a Fencing Contracting company in Melbourne Australia. We supply and install Timer and Steel boundary fences as well as Pool fencing (e.g. glass, tubular steel). We also manufacture and install swing and sliding gates.

We want a new website that is a modern business website.
We are targeting domestic and business clients.
The design should compliment our logo and company name.
The website needs to be easy to update.

Some specifics we want.
Menu - Main menu at top of page and smaller footer menu (to add different menu items)
Slider - Main page to have a slider on it that's easy for us to add and remove slides.
Call to action - all pages to have a "call to action" logo or icon that attracts attention (see file "call_to_action.pdf)
Instant quote - we have a online quote page we need a distinctive logo or icon to redirect to this page.
Main page to have a product /Service guide (see file "website_idea.jpg")
Main page to have widgets or quick link to
o why choose us
o Brochures
o Gallery

Have a Gallery page formatted with different category galleries. e.g. Timber, Glass, Feature
Maintain the current link to our staff page with password, (link in footer menu)

Hopefully that covers everything.
Our current website is www.tallwattlefencing.com.au to have a look at the current site.
regards Doug

• Turn off blogging as we don’t want 100’s of comments from spammers to delete

We would like to implement the PortalNest plugin (see "http://portalnest-example.com/" ), but this can be done after the new Theme has been implemented.

```html
<!DOCTYPE html>
<html lang="en">
<head>
<meta charset="utf-8">
<title>Tall Wattle Fencing</title>
<link href="https://fonts.googleapis.com/css2?family=Montserrat:wght@400;600;700&family=Open+Sans:wght@400;600;700&display=swap" rel="stylesheet">
<style>
:root{
  --red:#9b1a1e;
  --ink:#222;
  --text:#555;
  --black:#111;
  --footer:#1b1b1b;
  --panel:#ececec;
  --white:#fff;
}
*{box-sizing:border-box;margin:0;padding:0}
html,body{width:742px;height:1200px;overflow:hidden;background:var(--white)}
body{position:relative;font-family:"Open Sans",Arial,sans-serif;color:var(--text)}
.site-header{position:absolute;left:0;top:0;width:742px;height:62px;border-bottom:3px solid var(--red)}
.brand{position:absolute;left:81px;top:14px;display:flex;align-items:center;gap:6px;font-family:"Montserrat",sans-serif;font-weight:700;font-size:15px;color:var(--red)}
.brand-mark{width:14px;height:14px;background:var(--red)}
.office{position:absolute;left:533px;top:8px;width:128px;height:20px;background:#222;color:var(--white);font-family:"Montserrat",sans-serif;font-size:8px;font-weight:700;display:flex;align-items:center;padding-left:32px}
.office-icon{position:absolute;left:2px;top:-1px;width:22px;height:22px;background:#e8891c;border-radius:3px;display:flex;align-items:center;justify-content:center}
.main-nav{position:absolute;left:245px;top:33px;display:flex;font-family:"Montserrat",sans-serif;font-size:10px}
.main-nav a{color:#333;text-decoration:none;padding:0 7px;height:26px;line-height:27px}
.main-nav a.active{background:var(--red);color:var(--white);border-radius:4px 4px 0 0;padding:0 8px}
.hero{position:absolute;left:0;top:62px;width:742px;height:311px;background:linear-gradient(180deg,#3f5a2a 0%,#6f8a4a 45%,#d9dcd6 62%,#b8b3a8 100%)}
.slider-dots{position:absolute;right:82px;bottom:11px;display:flex;gap:3px}
.slider-dots span{width:9px;height:9px;border-radius:50%;background:var(--white)}
.slider-dots span.on{background:var(--red)}
.features{position:absolute;left:0;top:373px;width:742px;height:321px;background:var(--red)}
.card{position:absolute;top:25px;width:176px;height:263px;background:linear-gradient(180deg,#fff 80%,#ececec);border-radius:3px;text-align:center}
.card-img{position:absolute;left:8px;top:8px;width:160px;height:110px}
.card h2{position:absolute;top:126px;width:100%;font-family:"Montserrat",sans-serif;font-size:15px;font-weight:600;color:var(--ink)}
.card p{position:absolute;top:157px;left:14px;right:14px;font-size:8.2px;line-height:12px;color:#666}
.card-btn{position:absolute;left:40px;bottom:-10px;width:93px;height:20px;background:var(--black);color:var(--white);border-radius:10px;font-size:8px;display:flex;align-items:center;justify-content:center;gap:6px}
.card-btn b{font-size:13px;line-height:1}
.welcome{position:absolute;left:81px;top:714px;width:362px}
.welcome h1{font-family:"Montserrat",sans-serif;font-size:14.5px;color:var(--red);font-weight:700;margin-bottom:13px}
.welcome p{font-size:8.5px;line-height:13.5px;margin-bottom:13px}
.welcome h3{font-family:"Montserrat",sans-serif;font-size:9.5px;color:var(--ink);margin:25px 0 7px;font-weight:600}
.services{position:absolute;left:486px;top:718px;width:174px;height:246px;background:var(--panel);box-shadow:1px 2px 3px rgba(0,0,0,.2);padding:9px 11px}
.services h2{font-family:"Montserrat",sans-serif;color:var(--red);font-size:14px;font-weight:700;margin-bottom:6px}
.services li{list-style:none;font-size:8.5px;color:#444;height:20.8px;display:flex;align-items:center;gap:7px}
.quote-btn{position:absolute;left:486px;top:990px;width:174px;height:46px;background:linear-gradient(180deg,#ec5a2a,#c9340f);border-radius:3px;box-shadow:0 2px 2px rgba(0,0,0,.25);color:var(--white);font-family:"Montserrat",sans-serif;font-weight:600;font-size:16px;display:flex;align-items:center;padding-left:11px;gap:9px}
.site-footer{position:absolute;left:0;top:1098px;width:742px;height:102px;background:var(--footer);color:#bbb;font-size:8px}
.site-footer h4{color:var(--white);font-family:"Montserrat",sans-serif;font-size:9px;font-weight:600;margin-bottom:4px}
.f-links{position:absolute;left:81px;top:15px}
.f-gallery{position:absolute;left:81px;top:53px}
.f-contact{position:absolute;left:485px;top:15px}
.social{display:flex;gap:5px;margin-top:4px}
.social span{width:18px;height:18px;border-radius:50%;background:#555}
.copy{position:absolute;left:485px;top:76px}
</style>
</head>
<body>
<header class="site-header">
  <div class="brand"><span class="brand-mark"></span>Tall Wattle Fencing</div>
  <div class="office"><span class="office-icon"><svg width="12" height="12" viewBox="0 0 24 24"><path fill="#222" d="M6.6 10.8a15 15 0 0 0 6.6 6.6l2.2-2.2c.3-.3.7-.4 1-.2 1.1.4 2.3.6 3.6.6.6 0 1 .4 1 1V20c0 .6-.4 1-1 1A17 17 0 0 1 3 4c0-.6.4-1 1-1h3.5c.6 0 1 .4 1 1 0 1.3.2 2.5.6 3.6.1.3 0 .7-.2 1z"/></svg></span>OFFICE : 03 9000 4127</div>
  <nav class="main-nav">
    <a class="active" href="#">Home</a><a href="#">Steelform</a><a href="#">Instant Quote</a><a href="#">Gallery</a><a href="#">Products &amp; Services</a><a href="#">Contact us</a>
  </nav>
</header>

<section class="hero" role="img" aria-label="Slide photo: white ornamental sliding gate between pillars, tropical garden behind">
  <div class="slider-dots"><span class="on"></span><span></span><span></span><span></span><span></span></div>
</section>

<section class="features">
  <article class="card" style="left:81px">
    <div class="card-img" role="img" aria-label="Photo of two children behind a white picket fence" style="background:linear-gradient(160deg,#6b8f4a,#c9c6b8 60%,#e8e6de)"></div>
    <h2>Why Choose Us</h2>
    <p>We offer a 12 month workmanship warranty on our fences and will clean the site for free of any fencing debris from the fence construction upon completion of the job. We can offer this workmanship warranty</p>
    <a class="card-btn">Find Out More <b>+</b></a>
  </article>
  <article class="card" style="left:283px">
    <div class="card-img" role="img" aria-label="Photo of a spiral-bound brochure" style="background:linear-gradient(150deg,#e6e6e6,#f3f3f3 50%,#c8cf6a 85%)"></div>
    <h2>Brochures</h2>
    <p>No pool is complete without a beautiful Pool fence. See our range of Tubular Fencing designs Download our Steelform Fencing Brochure and see what a fantastic addition to your home see what a fantastic addition to your home</p>
    <a class="card-btn">Download Here <b>+</b></a>
  </article>
  <article class="card" style="left:485px">
    <div class="card-img" role="img" aria-label="Photo of a house with a black steel driveway gate" style="background:linear-gradient(180deg,#b8cde0,#c9b48e 45%,#4f6a3a)"></div>
    <h2>Gallery</h2>
    <p>Please feel free to look through our gallery, these are jobs that we have personally done! Please feel free to look through our gallery, these are jobs that we have personally done! jobs that we have personally done!</p>
    <a class="card-btn">See Our Work <b>+</b></a>
  </article>
</section>

<main class="welcome">
  <h1>Welcome to Tall Wattle Fencing</h1>
  <p>Thank you for visiting us at Tall Wattle Fencing, my name is Doug and I am the Manager.<br>I built my first fence when I was in my early twenties and have been building fences ever since. Over the last few years we have spent the time looking for fantastic fencing contractors to join our team. Because we only accept the best we have built our business to be one of Victoria's largest fencing contractors.</p>
  <p>At Tall Wattle Fencing, we believe in quality above all. The first fence we constructed was over 25 years ago and the number one thing we have learnt is that to do the job right the first time is the best insurance against costly rework.</p>
  <h3>“Built right the first time, every time”</h3>
  <p>We offer a 12 month workmans http://tallwattlefencing.com.au/images/bt-arise/aboutus.jpg ip warranty on our fences and will clean the site for free of any debris from the fence construction upon completion of the job. We can offer this workmanship warranty because of our work practices, these include</p>
  <p>6KG of cement in each wooden fence post and 15 – 20KG of concrete for all Steel posts<br>90mm galvanised nails in all rail's rather than industry standard of 75mm<br>75mm galvanised nails in all plinth boards, rather than the industry standard 57mm<br>Timber and Steel all sourced from Industry leaders, rather than the cheapest we can get<br>Gates are all made to order, rather than off the rack. (this means it's always going to be a better fit)</p>
</main>

<aside class="services">
  <h2>Our Service</h2>
  <ul>
    <li><svg width="9" height="8" viewBox="0 0 10 8"><path d="M1 4l3 3 5-6" stroke="#aaa" stroke-width="2" fill="none"/></svg>Bathroom Remodeling</li>
    <li><svg width="9" height="8" viewBox="0 0 10 8"><path d="M1 4l3 3 5-6" stroke="#aaa" stroke-width="2" fill="none"/></svg>Attic &amp; Garage Finishing</li>
    <li><svg width="9" height="8" viewBox="0 0 10 8"><path d="M1 4l3 3 5-6" stroke="#aaa" stroke-width="2" fill="none"/></svg>Carpentry</li>
    <li><svg width="9" height="8" viewBox="0 0 10 8"><path d="M1 4l3 3 5-6" stroke="#aaa" stroke-width="2" fill="none"/></svg>Tile &amp; Flooring</li>
    <li><svg width="9" height="8" viewBox="0 0 10 8"><path d="M1 4l3 3 5-6" stroke="#aaa" stroke-width="2" fill="none"/></svg>Decks</li>
    <li><svg width="9" height="8" viewBox="0 0 10 8"><path d="M1 4l3 3 5-6" stroke="#aaa" stroke-width="2" fill="none"/></svg>General Home Maintenance</li>
    <li><svg width="9" height="8" viewBox="0 0 10 8"><path d="M1 4l3 3 5-6" stroke="#aaa" stroke-width="2" fill="none"/></svg>Painting &amp; Wall Treatments</li>
    <li><svg width="9" height="8" viewBox="0 0 10 8"><path d="M1 4l3 3 5-6" stroke="#aaa" stroke-width="2" fill="none"/></svg>Drywall Install</li>
    <li><svg width="9" height="8" viewBox="0 0 10 8"><path d="M1 4l3 3 5-6" stroke="#aaa" stroke-width="2" fill="none"/></svg>Electrical</li>
    <li><svg width="9" height="8" viewBox="0 0 10 8"><path d="M1 4l3 3 5-6" stroke="#aaa" stroke-width="2" fill="none"/></svg>Fences</li>
  </ul>
</aside>

<a class="quote-btn"><svg width="28" height="28" viewBox="0 0 28 28"><rect x="2" y="4" width="22" height="22" rx="3" fill="none" stroke="#fff" stroke-width="2.5"/><path d="M10 18l2-5 10-10 3 3-10 10z" fill="#fff"/></svg>Instant Quote</a>

<footer class="site-footer">
  <div class="f-links"><h4>Quick Links</h4>Home &nbsp;|&nbsp; Steelform &nbsp;|&nbsp; Instant Quote &nbsp;|&nbsp; Gallery &nbsp;|&nbsp; Products &amp; Services &nbsp;|&nbsp; Contact us</div>
  <div class="f-gallery"><h4>Gallery Links</h4>Timber &nbsp;|&nbsp; Glass</div>
  <div class="f-contact"><h4>Get In Touch</h4>Office : 03 9000 4127
    <div class="social"><span></span><span></span><span></span><span></span></div>
  </div>
  <div class="copy">Copyright © 2013 Tall Wattle Fencing.com.au</div>
</footer>
</body>
</html>
```